Mini Book (4.25 x 6) Cover Design for Christian authors

We need a book cover designed for a mini book (4.25 x 6). We will need a front, back and spine for the book.
The book is titled:
Harbor Lanterns
Subtitle:
Divine Significance in Your Name
Authors:
Walter and Renata Oskarsby
We are wanting the colors Dark Blue and Grey with more blue than grey.
We do not want any stock images or photos, only original work.
The cover should convey sincerity, intuition and truth with prestige.
We want the back cover text to be included (top) and the bios to be on the back as well (bottom). *Those documents are included in the files.
Since it is a mini book, it is important for the design to be simple and not cluttered, but powerful!
This is the first book in a twelve book series, so we would like the same "look" to carry through all twelve books, eventually.
On the back of the book, at the bottom (left), we want the following contact information:
Bright Meadow Method Logo (in files below)
tallwillowstudio@mailfernly.com
303.512.4086
P.O.Box 718
Sedalia, CO 80417

Please save room on the back (bottom-right) for the ISBN and price.
Updates

Thank you to the designers that have submitted feedback concerning our design brief. We have made some changes that will perhaps make it easier to submit a variety of designs.Thank you! Added Saturday, March 4, 2017

Target Market(s)

Christians - mainly women

Industry/Entity Type

Religious

Font styles to use
Serif
Sans Serif
Decorative
Script
Other font styles liked:
• Not any particular font, looking for one that goes well with the cover design.

Requirements
Must have
• Mini Book Size (4.25 x 6)-spine size 1/8" (0.125)
• Dark blue and grey colors
• Cover needs to be simple and not cluttered or busy.
• Intriguing
• A font that is attractive, but it is still easy to read.
• *File information below
Nice to have
• Designs that are different from the mainstream.
• Perhaps a design that would do something different with the title/font? Maybe a repeat of the words from smaller to larger? Not sure how it would look, but maybe?
Should not have
• Any other colors but dark blue and grey
• Cluttered Look

```html
<!DOCTYPE html>
<html lang="en">
<head>
<meta charset="utf-8">
<title>Harbor Lanterns – Book Cover</title>
<link rel="stylesheet" href="https://fonts.googleapis.com/css2?family=IM+Fell+English+SC&family=Cinzel:wght@400;500&family=EB+Garamond:ital,wght@0,400;1,400&display=swap">
<style>
  :root {
    --page-bg: #ececec;
    --cover-blue: #2a1cc2;
    --cover-blue-deep: #1c1494;
    --cover-blue-light: #3a30d4;
    --ink-white: #ffffff;
    --ink-soft: #d9dbee;
    --ink-grey: #c9c9cf;
    --box-grey: #c8c8c8;
  }
  * { margin: 0; padding: 0; box-sizing: border-box; }
  html, body {
    width: 1200px; height: 801px; overflow: hidden;
    background: var(--page-bg);
  }
  .jacket {
    position: absolute; left: 132px; top: 82px;
    width: 936px; height: 640px;
    display: flex;
    box-shadow: 0 10px 30px rgba(0,0,0,.18);
  }
  .panel {
    position: relative; height: 100%; overflow: hidden;
    background:
      radial-gradient(ellipse at 30% 75%, rgba(20,10,110,.35), transparent 55%),
      radial-gradient(ellipse at 75% 25%, rgba(70,60,230,.25), transparent 50%),
      radial-gradient(ellipse at 60% 90%, rgba(20,10,120,.3), transparent 45%),
      var(--cover-blue);
    color: var(--ink-white);
  }
  .back-cover, .front-cover { width: 460px; }
  .spine {
    width: 16px;
    background: linear-gradient(90deg, var(--cover-blue-deep), var(--cover-blue-light), var(--cover-blue-deep));
    display: flex; align-items: center; justify-content: center;
  }
  .spine-text {
    writing-mode: vertical-rl;
    font-family: "Cinzel", serif; font-size: 9px; letter-spacing: 2px;
    color: var(--ink-soft); white-space: nowrap;
  }
  .spine-title { font-family: "IM Fell English SC", serif; font-size: 11px; margin-bottom: 18px; color: var(--ink-white); }
  .spine-authors { margin-top: 120px; }

  /* Front */
  .front-cover { text-align: center; }
  .subtitle {
    position: absolute; top: 40px; left: 0; right: 0;
    font-family: "EB Garamond", serif; font-style: italic; font-size: 20px;
    color: var(--ink-white);
  }
  .title-main {
    position: absolute; top: 176px; left: 0; right: 0;
    font-family: "IM Fell English SC", serif; font-size: 82px; line-height: 1;
    font-weight: 400; white-space: nowrap;
  }
  .title-sub {
    position: absolute; top: 290px; left: 0; right: 0;
    font-family: "Cinzel", serif; font-size: 32px; letter-spacing: 5px;
    font-weight: 400; color: var(--ink-grey);
  }
  .authors {
    position: absolute; bottom: 40px; left: 0; right: 0;
    font-family: "Cinzel", serif; color: var(--ink-grey);
  }
  .authors-first { font-size: 24px; letter-spacing: 2px; }
  .authors-last { font-size: 18px; letter-spacing: 2px; margin-top: 2px; }

  /* Back */
  .back-copy {
    position: absolute; top: 42px; left: 34px; right: 34px;
    font-family: "EB Garamond", serif; font-size: 11.5px; line-height: 1.3;
    color: var(--ink-soft); text-align: justify;
  }
  .back-copy p + p, .back-copy ul + p { margin-top: 14px; }
  .benefits { list-style: none; margin-top: 2px; }
  .benefits li::before { content: "• "; }
  .scripture {
    position: absolute; top: 438px; left: 34px; right: 34px;
    font-family: "EB Garamond", serif; font-size: 11.5px; line-height: 1.3;
    text-align: center; color: var(--ink-soft);
  }
  .back-footer {
    position: absolute; bottom: 34px; left: 34px; right: 34px;
    display: flex; justify-content: space-between; align-items: flex-end;
  }
  .publisher-mark {
    width: 100px; height: 74px; background: var(--ink-white);
    display: flex; align-items: center; justify-content: center;
    font-family: "EB Garamond", serif; font-size: 13px; color: var(--cover-blue);
  }
  .isbn-box { width: 118px; height: 74px; background: var(--box-grey); }
</style>
</head>
<body>
  <div class="jacket">
    <section class="panel back-cover">
      <div class="back-copy">
        <p>God always has our best interest at heart. Bright Meadow Method (BMM) gives us Strength, Confidence and Grit to persevere through the many challenges we face, and it prepares and propels us into our Divine Inheritance. By understanding the power that He has given to us, we are able to significantly impact the lives of others by fulfilling our own Blessed Destiny of being a blessing to others.</p>
        <p>This book will help you:</p>
        <ul class="benefits">
          <li>Uncover the secret that is God’s plan</li>
          <li>Seek Divine revelation of the BMM for your specific situation</li>
          <li>Significantly impact the lives of others by fulfilling your own Blessed Destiny</li>
          <li>Discover the path you are meant to be on</li>
          <li>Recognize God’s imprint on your life and the importance of leaving your imprint on others</li>
        </ul>
        <p>Renata and Walter Oskarsby are international award-winning authors who inspire couples and individuals to connect to the heart of God through Bright Meadow Method. For over twenty years, they have conducted workshops and seminars throughout the country and at their private retreat center located in the Colorado mountains.</p>
      </div>
      <blockquote class="scripture">
        “Come, let us go up to the mountain of the LORD,<br>
        To the house (temple) of the God of Jacob;<br>
        That He may teach us His ways<br>
        And that we may walk in His paths.”<br>
        - Isaiah 2:3 -
      </blockquote>
      <div class="back-footer">
        <div class="publisher-mark">Kindred Letters</div>
        <div class="isbn-box" aria-label="Space for ISBN and price"></div>
      </div>
    </section>

    <div class="panel spine">
      <div class="spine-text">
        <span class="spine-title">HARBOR LANTERNS</span>
        <span class="spine-authors">WALTER &amp; RENATA OSKARSBY</span>
      </div>
    </div>

    <section class="panel front-cover">
      <p class="subtitle">Divine Significance in Your Name</p>
      <h1 class="title-main">HARBOR</h1>
      <h2 class="title-sub">LANTERNS</h2>
      <div class="authors">
        <div class="authors-first">WALTER &amp; RENATA</div>
        <div class="authors-last">OSKARSBY</div>
      </div>
    </section>
  </div>
</body>
</html>
```